www.HarborviewSmileGlow.com needs to be re-designed

Current website to be redesigned www.HarborviewSmileGlow.com

*Need a custom-made new theme

I need all 10 pages redesigned using existing content.
I need the website to be revamped to a more modern look.

Please start with Homepage first then after homepage mock up is approved we can move forward with rest of pages.

Please use existing images from my Facebook or Instagram page of our real customers for banner image...

(Where to find my FB and IG pages...
You can access these pages from the website header and "contact us" page for address.)

I would like to have a button that says "Book Appointment Online" and get rid of the actual form that is on current website.

But other than that please include all other content, features, etc in mock ups so I can make a decision on the website.

I prefer custom design and must be WP installable responsive theme.

This is design-only. I am open to any concepts you can submit.

Target Market(s)

people that care about thier looks

Industry/Entity Type

Dental Clinic

Colors

Designer to choose colors to be used in the design.

Requirements
Must have
• All current content/text that is currently on website. Just formatted so it doesnt look so busy. I want to make emphasis on BOOK APPOINTMENT button and $99 SPECIAL BUTTON
Nice to have
• White background so everything pops
Should not have
• I do not like stock photo images, please use images from my facebook and IG page of real customers or even a snap shot of our office building. You can access these pages from the website header and contact us page for address, maybe yu can use snapshot somewhere of building of our address on homepage possibly in banner image.

```html
<!DOCTYPE html>
<html lang="en">
<head>
<meta charset="utf-8">
<title>Harborview Smile Glow</title>
<link href="https://fonts.googleapis.com/css2?family=Montserrat:wght@400;500;600;700&family=Open+Sans:wght@400;600;700&family=Allura&display=swap" rel="stylesheet">
<style>
:root{
  --navy:#0c3a63;
  --navy-dark:#0a2f50;
  --sky:#3bb8d6;
  --sky-light:#dcf0fa;
  --yellow:#f8c51c;
  --red:#e8401f;
  --text:#333;
  --muted:#777;
  --grey-bg:#f1f1f1;
  --white:#fff;
}
*{box-sizing:border-box;margin:0;padding:0}
html,body{width:1200px;height:3197px;overflow:hidden;background:var(--white)}
body{position:relative;font-family:"Open Sans",sans-serif;color:var(--text);font-size:13px}
.abs{position:absolute}
.promo-bar{left:0;width:1200px;height:42px;background:var(--yellow);display:flex;align-items:center;justify-content:center;gap:22px;font-family:"Montserrat",sans-serif;font-weight:600;font-size:16px;color:#111}
.promo-bar .price{color:var(--red)}
.btn-book{background:var(--red);color:#fff;border-radius:20px;padding:7px 10px 7px 18px;font-size:14px;font-weight:600;display:inline-flex;align-items:center;gap:8px}
.btn-book .arrow{width:20px;height:20px;border-radius:50%;background:#fff;color:var(--red);display:flex;align-items:center;justify-content:center;font-size:12px;font-weight:700}
.site-header{top:42px;left:0;width:1200px;height:112px}
.brand{left:110px;top:28px;display:flex;align-items:center;gap:12px}
.brand-mark{width:52px;height:52px;border-radius:50%;background:var(--sky-light);border:2px solid var(--sky)}
.brand-name{font-family:"Montserrat",sans-serif;font-weight:700;font-size:22px;color:var(--navy);line-height:1.1}
.info{display:flex;gap:12px;top:28px}
.info svg{flex:none}
.info-text{font-size:12px;color:var(--muted);line-height:1.45}
.info-text b{color:#222;font-weight:600;font-size:14px}
.main-nav{top:154px;left:0;width:1200px;height:42px;background:var(--navy);display:flex;padding-left:110px}
.main-nav a{color:#fff;text-decoration:none;font-family:"Montserrat",sans-serif;font-weight:600;font-size:13px;padding:0 14px;line-height:42px}
.main-nav a.active{background:var(--sky)}
.hero{top:196px;left:0;width:1200px;height:514px;background:linear-gradient(180deg,#cfeaf8 0%,#e7f5fc 55%,#d2ecf8 100%);overflow:hidden}
.hero-photo{right:0;top:0;width:440px;height:514px;background:linear-gradient(90deg,rgba(233,200,180,0) 0%,#f0cfba 35%,#e6b497 70%,#f3d9c8 100%)}
.hero-title{left:145px;top:78px;font-family:"Montserrat",sans-serif;font-weight:700;color:var(--navy);font-size:40px;line-height:50px}
.hero-title .script{font-family:"Allura",cursive;font-weight:400;font-size:66px;line-height:0;color:#fff;text-shadow:0 0 2px var(--sky),0 0 1px var(--sky)}
.hero-title .line2{display:block;padding-left:110px}
.call-strip{left:0;top:240px;width:768px;height:24px;background:var(--navy);color:#fff;font-family:"Montserrat",sans-serif;font-weight:700;font-size:14px;letter-spacing:2px;text-align:right;padding-right:50px;line-height:24px}
.hero-phone{left:302px;top:270px;font-family:"Montserrat",sans-serif;font-size:40px;color:var(--navy);font-weight:400}
.features{top:392px;left:125px;display:flex;gap:50px}
.feature{display:flex;align-items:center;gap:14px;font-family:"Montserrat",sans-serif;font-size:14px;color:var(--navy);line-height:1.3;width:210px}
.feature-icon{width:56px;height:56px;border-radius:50%;background:#fff;display:flex;align-items:center;justify-content:center;box-shadow:0 2px 6px rgba(0,0,0,.08)}
.intro{top:710px;left:0;width:1200px;height:387px;background:var(--grey-bg)}
.intro-text{left:110px;top:50px;width:470px}
h2.section-title{font-family:"Montserrat",sans-serif;font-weight:700;font-size:20px;color:#222}
.subtitle{color:var(--sky);font-weight:700;font-size:14px;margin:6px 0 16px}
.intro-text p,.how-text p{font-size:12.5px;line-height:1.7;color:var(--muted);margin-bottom:16px}
.video{left:618px;top:58px;width:462px;height:272px;background:#fff;padding:10px;box-shadow:0 2px 8px rgba(0,0,0,.15)}
.video-inner{width:100%;height:100%;background:radial-gradient(circle,#fafafa,#d9d9d9);display:flex;align-items:center;justify-content:center;gap:14px}
.video-title{font-family:"Montserrat",sans-serif;font-weight:700;font-size:24px;color:var(--navy)}
.how{top:1097px;left:0;width:1200px;height:512px}
.how-photo{left:0;top:33px;width:575px;height:472px;background:linear-gradient(180deg,#eef1f4 0%,#d8c5c0 50%,#7a2a45 100%)}
.how-text{left:612px;top:46px;width:476px}
.how-text h2{font-size:18px;margin-bottom:18px}
.strip{top:1609px;left:0;width:1200px;height:139px;display:flex;gap:3px}
.strip div{flex:1}
.compare{top:1748px;left:0;width:1200px;height:560px;background:linear-gradient(180deg,#cfe9f5 0%,#f3fafd 40%,#cbe6f3 100%)}
.compare h2{position:absolute;top:48px;width:100%;text-align:center;font-size:20px}
table.compare-table{position:absolute;left:117px;top:106px;width:963px;border-collapse:collapse;box-shadow:0 6px 18px rgba(0,0,0,.15);background:#fff;font-family:"Montserrat",sans-serif}
.compare-table th{height:70px;font-size:19px;font-weight:600;color:#fff;background:var(--sky);border-right:2px solid #fff}
.compare-table th.lead{background:var(--navy)}
.compare-table th.ours{background:#fff;color:var(--navy);font-size:15px}
.compare-table td{height:43px;text-align:center;font-size:12px;color:#555;border-top:1px solid #e5e5e5;border-right:2px solid #fff}
.compare-table td:first-child{font-weight:600;color:#333;font-size:13px}
.compare-table tr:nth-child(odd) td{background:#f3f3f3}
.compare-table tr:nth-child(even) td{background:#e6e6e6}
.compare-table tr.cost td{font-size:19px;font-weight:600;color:#222;height:58px}
.compare-table tr.cost td:first-child{font-size:13px}
.compare-table th:first-child,.compare-table td:first-child{width:193px}
.cta-row{top:2222px;left:0;width:1200px;display:flex;justify-content:center;gap:22px;align-items:center;font-family:"Montserrat",sans-serif;font-weight:600;font-size:16px}
.cta-row .price{color:var(--red)}
.why{top:2308px;left:0;width:1200px;height:138px;background:#e9ecee}
.why h3{position:absolute;left:110px;top:56px;font-family:"Montserrat",sans-serif;font-weight:700;font-size:17px;color:#222}
.why-band{position:absolute;left:298px;top:0;width:789px;height:138px;display:flex;overflow:hidden}
.why-item{flex:1;background:var(--navy);transform:skewX(-12deg);margin-right:3px;display:flex;align-items:center;justify-content:center}
.why-item>div{transform:skewX(12deg);text-align:center;color:#fff;font-family:"Montserrat",sans-serif;font-weight:700;font-size:14px}
.why-item svg{display:block;margin:0 auto 14px}
.col-title{font-family:"Montserrat",sans-serif;font-weight:700;font-size:18px;color:#222;display:flex;align-items:center;gap:10px}
.col-title::after{content:"";flex:1;height:3px;background:var(--sky)}
.blog{left:110px;top:2484px;width:300px}
.post{margin-top:22px}
.post .meta{font-size:10px;color:#888}
.post .meta span{color:var(--sky)}
.post p{font-size:14px;font-weight:600;color:#222;line-height:1.35;margin-top:4px}
.gallery{left:447px;top:2484px;width:310px}
.gallery-grid{display:grid;grid-template-columns:1fr 1fr;gap:6px;margin-top:14px}
.gallery-grid div{height:108px;background:linear-gradient(180deg,#b76a6a,#efe5d8 55%,#c47a76)}
.btn-photos{margin-top:10px;background:var(--sky);color:#fff;text-align:center;font-weight:700;font-size:14px;line-height:42px;border-radius:4px}
.testimonials{left:780px;top:2484px;width:310px}
.quote-box{margin-top:22px;background:#f1f1f1;padding:22px 22px 22px 60px;position:relative;font-size:12.5px;line-height:1.6;color:#666}
.quote-box .mark{position:absolute;left:22px;top:14px;font-size:36px;color:var(--sky);font-family:Georgia,serif;line-height:1}
.quote-author{margin:22px 0 0 60px;font-weight:600;font-size:14px;color:#222}
.footer{top:2941px;left:0;width:1200px;height:256px;background:var(--navy);color:#c9d6e2}
.footer-mark{left:110px;top:44px;width:100px;height:100px;border-radius:50%;background:#1d5384;border:3px solid #fff}
.footer h4{font-family:"Montserrat",sans-serif;font-weight:700;color:#fff;font-size:13px;margin-bottom:18px}
.links{left:278px;top:32px}
.links ul{list-style:none;display:grid;grid-template-columns:142px 140px;row-gap:8px;font-size:12px}
.contact{left:582px;top:32px;font-size:12px;line-height:1.55}
.newsletter{left:864px;top:32px;width:225px}
.newsletter .field{height:34px;border-radius:17px;background:#fff;color:#999;font-size:12px;line-height:34px;padding-left:16px}
.newsletter .btn{margin-top:10px;width:112px;height:34px;border-radius:17px;background:var(--sky);color:#fff;font-weight:700;font-size:11px;text-align:center;line-height:34px}
.footer-bottom{left:110px;top:208px;width:980px;display:flex;justify-content:space-between;align-items:center;font-size:12px}
.social{display:flex;gap:8px}
.social span{width:26px;height:26px;border:1.5px solid #c9d6e2;border-radius:50%}
</style>
</head>
<body>

<div class="abs promo-bar" style="top:0">
  <span>Click Here To Get Our <span class="price">$99</span> Teeth Whitening Deal (Reg $378)</span>
  <span class="btn-book">Book Appointment Online <span class="arrow">&#10095;</span></span>
</div>

<header class="abs site-header">
  <div class="abs brand">
    <span class="brand-mark"></span>
    <span class="brand-name">Harborview<br>Smile Glow</span>
  </div>
  <div class="abs info" style="left:428px">
    <svg width="26" height="44" viewBox="0 0 26 44"><rect x="1" y="1" width="24" height="42" rx="5" fill="none" stroke="#3bb8d6" stroke-width="2"/><circle cx="13" cy="36" r="2.5" fill="#3bb8d6"/></svg>
    <div class="info-text"><b>Book Appointment</b><br>Mon-Fri : 8:30am to 5:00pm<br>Sat-Sun : Closed</div>
  </div>
  <div class="abs info" style="left:666px">
    <svg width="26" height="44" viewBox="0 0 26 44"><rect x="1" y="1" width="24" height="42" rx="5" fill="none" stroke="#3bb8d6" stroke-width="2"/><circle cx="13" cy="36" r="2.5" fill="#3bb8d6"/></svg>
    <div class="info-text"><b>Clinic Hours</b><br>Mon-Fri : 9:15am to 5:30pm<br>Sat : 10am to 2pm (Sun: Closed)</div>
  </div>
  <div class="abs info" style="left:912px">
    <svg width="26" height="44" viewBox="0 0 26 44"><rect x="1" y="1" width="24" height="42" rx="5" fill="none" stroke="#3bb8d6" stroke-width="2"/><circle cx="13" cy="36" r="2.5" fill="#3bb8d6"/></svg>
    <div class="info-text">Teeth Whitening Center<br>Call Now! Today<br><b>555-214-7730</b></div>
  </div>
</header>

<nav class="abs main-nav">
  <a class="active">Home</a><a>Our Process</a><a>Photos</a><a>White Smile Club</a><a>Testimonials</a><a>Appointments</a><a>FAQ</a><a>Contact Us</a><a>Blog</a><a>Buy Now</a>
</nav>

<section class="abs hero">
  <div class="abs hero-photo" role="img" aria-label="Photo of a smiling client with freshly whitened teeth"></div>
  <h1 class="abs hero-title">Get That <span class="script">White Smile</span><span class="line2">You've Always Wanted</span></h1>
  <div class="abs call-strip">GIVE US A CALL TO SCHEDULE AN APPOINTMENT</div>
  <div class="abs hero-phone">555-214-7730</div>
  <div class="abs features">
    <div class="feature"><span class="feature-icon"><svg width="28" height="28" viewBox="0 0 28 28"><path d="M7 6c3-2 5 0 7 0s4-2 7 0c2 2 1 7-1 10l-2 8-2-6h-4l-2 6-2-8C5 13 5 8 7 6z" fill="none" stroke="#3bb8d6" stroke-width="2"/></svg></span>Amazing<br>Results</div>
    <div class="feature"><span class="feature-icon"><svg width="28" height="28" viewBox="0 0 28 28"><circle cx="14" cy="14" r="10" fill="none" stroke="#3bb8d6" stroke-width="2"/><path d="M9 14l4 4 6-8" fill="none" stroke="#3bb8d6" stroke-width="2"/></svg></span>The Most<br>Effective System</div>
    <div class="feature"><span class="feature-icon"><svg width="28" height="28" viewBox="0 0 28 28"><path d="M4 12c4-4 16-4 20 0-4 8-16 8-20 0z" fill="none" stroke="#3bb8d6" stroke-width="2"/><path d="M8 12h12" stroke="#3bb8d6" stroke-width="2"/></svg></span>More Affordable<br>Than The Dentist</div>
  </div>
</section>

<section class="abs intro">
  <div class="abs intro-text">
    <h2 class="section-title">Harborview Smile Glow</h2>
    <div class="subtitle">The best price, service and results.</div>
    <p>Harborview Smile Glow features state-of-the-art technologies that are safe, industry-unique and very cost-effective. Our teeth whitening system utilizes the latest blue light whitening technology. Our Blue Light Systems are calibrated precisely for optimal activation of our exclusive hydrogen peroxide based whitening solution which is manufactured in a FDA registered facility in the USA.</p>
    <p>Our special lighting systems intensify the release of hydroxyl radicals that accelerate the dissipation of tooth stains. The entire teeth whitening process is accelerated and able to be completed in just 45 minutes with instant results.</p>
  </div>
  <div class="abs video">
    <div class="video-inner">
      <span class="video-title">Harborview Smile Glow</span>
      <svg width="40" height="40" viewBox="0 0 40 40" aria-label="Play video"><circle cx="20" cy="20" r="18" fill="none" stroke="#0c3a63" stroke-width="2"/><path d="M16 13l11 7-11 7z" fill="#0c3a63"/></svg>
    </div>
  </div>
</section>

<section class="abs how">
  <div class="abs how-photo" role="img" aria-label="Photo of the clinic team with a happy client in the office"></div>
  <div class="abs how-text">
    <h2 class="section-title">How It Works</h2>
    <p>We have a very effective teeth whitening treatment that is guaranteed to get you quick results in about 1 hour. To start the treatment you'll apply a Hydrogen Peroxide based whitening agent to your teeth. We then place our cold blue light directly in front of your exposed teeth for 15 minutes per treatment. The lighting systems we use activate the whitening agent and thats what accelerates the whitening process, giving you whiter teeth in less than an hour.</p>
    <p>We always perform what we call a "Triple Treatment". So that's 3 of the 15 minute treatments all done consecutively, in the same visit. The actual whitening time is a total of 45 minutes. Now there is a few minute break in between each 15 minute treatment and this is why we tell all of our patients to give yourself one hour at the office. The biggest benefit of doing an in office treatment vs a take home kit is that you will see results immediately after the treatment. We also include our home maintenance kit for after care. It's very important that no matter where you get your teeth whitened, you need to maintain them for long lasting results. You'll use our maintenance kit once or twice per month as a touch up to help maintain your newly whitened teeth, and that ultimately make your results last longer.</p>
  </div>
</section>

<div class="abs strip">
  <div role="img" aria-label="Photo of the clinic reception" style="background:linear-gradient(135deg,#e8e8e8,#b9b2ad)"></div>
  <div role="img" aria-label="Photo of a client during treatment" style="background:linear-gradient(135deg,#d9d2cc,#8a7466)"></div>
  <div role="img" aria-label="Photo of a client checking shade results" style="background:linear-gradient(135deg,#e2d6ce,#9b7a68)"></div>
  <div role="img" aria-label="Photo of a shade guide held to a client's teeth" style="background:linear-gradient(135deg,#d8cfc9,#7e6658)"></div>
  <div role="img" aria-label="Photo of a client under the blue whitening light" style="background:linear-gradient(135deg,#6a74c9,#2b2f5a)"></div>
</div>

<section class="abs compare">
  <h2 class="section-title">Compare Us</h2>
  <table class="compare-table">
    <tr><th class="lead">Features</th><th>LumaPro</th><th class="ours">Harborview</th><th>ClearBright</th><th>Home Kits</th></tr>
    <tr class="cost"><td>Cost</td><td>$300-$600</td><td>$378</td><td>$300-$600</td><td>$50-$150</td></tr>
    <tr><td>Speed</td><td>1-2 Hours</td><td>45 Mins</td><td>7-14 Days</td><td>7-30 Days</td></tr>
    <tr><td>Ease Of Use</td><td>Difficult/Dentist</td><td>Very Easy</td><td>Difficult</td><td>Difficult</td></tr>
    <tr><td>Availability</td><td>Limited Availability</td><td>Appt Only</td><td>Limited Availability</td><td>Store Purchase</td></tr>
    <tr><td>Pain</td><td>Pain &amp; Sensitivity</td><td>No Pain</td><td>Sensitivity</td><td>Sensitivity</td></tr>
  </table>
</section>

<div class="abs cta-row">
  <span>Click Here To Get Our <span class="price">$99</span> Teeth Whitening Deal (Reg $378)</span>
  <span class="btn-book">Book Appointment Online <span class="arrow">&#10095;</span></span>
</div>

<section class="abs why">
  <h3>Why Choose Us?</h3>
  <div class="why-band">
    <div class="why-item"><div><svg width="38" height="38" viewBox="0 0 38 38"><circle cx="19" cy="19" r="16" fill="none" stroke="#3bb8d6" stroke-width="2"/><text x="19" y="26" text-anchor="middle" fill="#3bb8d6" font-size="20" font-family="Montserrat,sans-serif">$</text></svg>Price</div></div>
    <div class="why-item"><div><svg width="38" height="38" viewBox="0 0 38 38"><rect x="6" y="4" width="26" height="30" fill="none" stroke="#3bb8d6" stroke-width="2"/><path d="M11 26l6-7 5 4 6-9" fill="none" stroke="#3bb8d6" stroke-width="2"/></svg>Results</div></div>
    <div class="why-item"><div><svg width="38" height="38" viewBox="0 0 38 38"><circle cx="19" cy="19" r="15" fill="none" stroke="#3bb8d6" stroke-width="2"/><path d="M8 30L30 8" stroke="#3bb8d6" stroke-width="2"/></svg>No Pain</div></div>
    <div class="why-item"><div><svg width="38" height="38" viewBox="0 0 38 38"><circle cx="19" cy="19" r="6" fill="none" stroke="#3bb8d6" stroke-width="2"/><circle cx="19" cy="19" r="13" fill="none" stroke="#3bb8d6" stroke-width="2" stroke-dasharray="5 3"/></svg>Service</div></div>
    <div class="why-item"><div><svg width="38" height="38" viewBox="0 0 38 38"><path d="M10 32V20c0-5 4-8 9-8h10" fill="none" stroke="#3bb8d6" stroke-width="2"/><path d="M24 6l6 6-6 6" fill="none" stroke="#3bb8d6" stroke-width="2"/></svg>Convenience</div></div>
  </div>
</section>

<section class="abs blog">
  <div class="col-title">From The Blog</div>
  <div class="post"><div class="meta">By <span>William Doe</span> | 20 Mar 2017 | 0 Comment</div><p>There are many variations of passages of but the majority available...</p></div>
  <div class="post"><div class="meta">By <span>William Doe</span> | 20 Mar 2017 | 0 Comment</div><p>There are many variations of passages of but the majority available...</p></div>
  <div class="post"><div class="meta">By <span>William Doe</span> | 20 Mar 2017 | 0 Comment</div><p>There are many variations of passages of but the majority available...</p></div>
</section>

<section class="abs gallery">
  <div class="col-title">Before &amp; After</div>
  <div class="gallery-grid">
    <div role="img" aria-label="Close-up of teeth before whitening"></div>
    <div role="img" aria-label="Close-up of teeth after whitening"></div>
    <div role="img" aria-label="Close-up of teeth before whitening"></div>
    <div role="img" aria-label="Close-up of teeth after whitening"></div>
  </div>
  <div class="btn-photos">See All Photos</div>
</section>

<section class="abs testimonials">
  <div class="col-title">Testimonials</div>
  <div class="quote-box"><span class="mark">&ldquo;</span>Thanks so much! Marco's mom did notice the difference in his teeth and she will be calling soon for an appointment. We are very happy with our results, and I love that Marco now smiles more often. We will visit again for maintenance before the six months pass.</div>
  <div class="quote-author">William Doe</div>
</section>

<div class="abs promo-bar" style="top:2870px;height:67px">
  <span>Click Here To Get Our <span class="price">$99</span> Teeth Whitening Deal (Reg $378)</span>
  <span class="btn-book">Book Appointment Online <span class="arrow">&#10095;</span></span>
</div>

<footer class="abs footer">
  <div class="abs footer-mark"></div>
  <div class="abs links">
    <h4>QUICK LINKS</h4>
    <ul><li>Home</li><li>Appointments</li><li>Our Process</li><li>FAQ</li><li>Photos</li><li>Contact</li><li>White Smile Club</li><li>Blog</li><li>Testimonials</li><li>Buy Now</li></ul>
  </div>
  <div class="abs contact">
    <h4>CONTACT INFO</h4>
    4170 Harbor Crest Blvd Ste 210,<br>Harborview, CA 90412<br><br>T: 555-318-4402<br>T: 888-555-0147
  </div>
  <div class="abs newsletter">
    <h4>SUBSCRIBE NEWSLETTER</h4>
    <div class="field">Name</div>
    <div class="btn">SUBSCRIBE</div>
  </div>
  <div class="abs footer-bottom">
    <span>&copy; 2017 Harborview Smile Glow. Terms of Use | Privacy | Sitemap</span>
    <div class="social"><span></span><span></span><span></span><span></span><span></span><span></span></div>
  </div>
</footer>

</body>
</html>
```